Technology Product Brochure Needed: Quillon KELP

We have an existing brochure that we need updated to reflect some recent rebranding. KELP is now known as Quillon KELP. The copy will be largely unchanged (we will provide a text document noting what can be trimmed and other sources you can examine). We have an updated logo, which we provided in two versions (regular and a more logo-like size), along with the brand colors. The layout can change completely, but still must be a tri-fold or bi-fold brochure. We ask that the designer use Adobe InDesign, because at the end of the project, we need the InDesign file for future copy updates. The BrandThe software is made by the IT company RVT, but we want to replace the RVT branding with Quillon branding. As part of our new Quillon line of software, we are really into the idea that pieces of data can fit together to make art. And that by putting all your data together, you can see the bigger picture. Quillon is the craft of records. And Quillon KELP is the craft of record transit. It's incredibly speedy. That's the main message. It's also easy to use. We want to get across the idea that anyone can perform this technical process, even if you don't know how to code. The visual message needs to be clean and easy to follow, yet interesting enough to impress people. Please note that there are other products in this line, and they each have an assigned color. So please do not use the Beacons or QTRx product colors as complements to the KELP color. It is okay to use the general/main Quillon color as complimentary. I included the KELP logo files below in PMS color as well as "black" and "white." We also have them available in CMYK and RGB. We prefer color to black or white but I included them in case you think one would make a neat background effect or something.
Target Market(s)
Business leaders
Industry/Entity Type
Software
Colors
Designer to choose colors to be used in the design.
Look and feel

```html
<!DOCTYPE html>
<html lang="en">
<head>
<meta charset="utf-8">
<title>Quillon KELP Tri-fold Brochure</title>
<link rel="stylesheet" href="https://fonts.googleapis.com/css2?family=Catamaran:wght@400;500;600;700;800&display=swap">
<style>
  :root {
    --stage: #9a9a9a;
    --purple: #5c4a94;
    --purple-mid: #7a69ae;
    --purple-soft: #9486c4;
    --purple-light: #b1a7d6;
    --ink: #1b1b22;
    --paper: #ffffff;
    --paper-grey: #ececee;
    --photo-deep: #1e2a4a;
    --photo-mid: #3d5a8a;
    --photo-light: #9db7d8;
  }
  * { box-sizing: border-box; margin: 0; padding: 0; }
  html, body { width: 1200px; height: 1200px; overflow: hidden; }
  body { background: var(--stage); font-family: "Catamaran", sans-serif; color: var(--ink); position: relative; }

  .spread { position: absolute; width: 701px; height: 545px; background: var(--paper); overflow: hidden; box-shadow: 0 3px 8px rgba(0,0,0,.35); }
  .spread--outside { left: 34px; top: 30px; }
  .spread--inside { left: 465px; top: 623px; }
  .panel { position: absolute; top: 0; height: 100%; overflow: hidden; }
  .photo { position: absolute; left: 0; top: 0; }
  .abs { position: absolute; }

  /* outside spread */
  .works { left: 0; width: 230px; background: linear-gradient(180deg, var(--purple-soft) 30%, var(--purple) 100%); }
  .works__title { left: 4px; top: 180px; font-size: 19px; font-weight: 700; color: #fff; }
  .works__copy { left: 5px; top: 207px; width: 218px; color: #fff; font-size: 10.6px; line-height: 14.3px; text-align: justify; }
  .works__copy p + p { margin-top: 14px; }

  .contact { left: 230px; width: 232px; background: linear-gradient(90deg, #e9e9ec, #fff 40%); }
  .brandmark { color: var(--purple); font-weight: 800; line-height: 1; }
  .brandmark__name { display: block; }
  .brandmark__product { display: block; text-align: right; font-weight: 800; }
  .contact .brandmark { left: 20px; top: 150px; width: 200px; }
  .contact .brandmark__name { font-size: 46px; letter-spacing: -1px; }
  .contact .brandmark__product { font-size: 19px; margin-top: 2px; }
  .contact__copy { left: 3px; top: 245px; width: 226px; text-align: center; font-size: 10px; line-height: 12.8px; font-weight: 600; }
  .contact__copy p + p { margin-top: 12px; }
  .contact__rule { left: 5px; top: 362px; width: 220px; border-top: 1px solid #999; }
  .contact__cta { left: 5px; top: 376px; width: 220px; text-align: center; font-size: 12px; font-weight: 700; line-height: 14px; }
  .contact__demo { left: 5px; top: 420px; width: 220px; text-align: center; font-size: 11px; line-height: 14px; }
  .contact__phone { left: 30px; top: 456px; font-size: 21px; font-weight: 800; display: flex; align-items: center; gap: 8px; }
  .band { position: absolute; left: 0; bottom: 0; width: 100%; height: 46px; background: var(--purple-soft); color: #fff; }
  .band__url { position: absolute; left: 0; width: 100%; text-align: center; top: 10px; font-size: 17px; font-weight: 700; }

  .cover { left: 462px; width: 239px; background: linear-gradient(90deg, #e7e7ea, #fff); }
  .cover .brandmark { left: 30px; top: 24px; width: 180px; }
  .cover .brandmark__name { font-size: 40px; letter-spacing: -1px; }
  .cover .brandmark__product { font-size: 17px; margin-top: 2px; }
  .cover__band { height: 46px; background: var(--purple-mid); }
  .cover__tag { position: absolute; width: 100%; text-align: center; top: 4px; font-size: 15.5px; font-weight: 500; }
  .cover__url { position: absolute; width: 100%; text-align: center; top: 26px; font-size: 9px; font-weight: 600; }

  /* inside spread */
  .intro { left: 0; width: 233px; background: linear-gradient(180deg, #f3f3f5, #e2e2e6); }
  .intro__title { left: 6px; top: 184px; font-size: 34px; font-weight: 700; color: var(--purple-mid); line-height: 1; }
  .intro__sub { left: 6px; top: 220px; font-size: 14px; font-weight: 600; color: var(--purple-soft); }
  .intro__copy { left: 8px; top: 251px; width: 220px; font-size: 10px; line-height: 13.6px; text-align: justify; }
  .intro__copy p + p { margin-top: 13px; }
  .intro .band { height: 32px; background: linear-gradient(90deg, var(--purple-mid), var(--purple-soft)); }
  .intro .band__url { top: 5px; font-size: 15px; font-weight: 600; }

  .benefits { left: 233px; width: 233px; background: linear-gradient(180deg, #fff, #f0f0f2); }
  .benefits__title { left: 4px; top: 138px; font-size: 26px; font-weight: 700; color: var(--purple-soft); line-height: 1; }
  .benefits__sub { left: 4px; top: 166px; font-size: 15px; font-weight: 700; color: var(--purple-soft); }
  .feature { position: absolute; left: 3px; width: 226px; }
  .feature + .feature { border-top: 1px solid #aaa; }
  .feature__head { font-size: 16px; font-weight: 700; line-height: 20px; }
  .checklist { list-style: none; margin-left: 8px; }
  .checklist li { position: relative; padding-left: 19px; font-size: 13.5px; line-height: 16px; margin-top: 4px; }
  .checklist li::before { content: ""; position: absolute; left: 2px; top: 2px; width: 5px; height: 9px; border: solid var(--purple-soft); border-width: 0 2.5px 2.5px 0; transform: rotate(40deg); }

  .mission { left: 466px; width: 235px; background: linear-gradient(180deg, #f2f2f4, #dcdce0); }
  .mission__banner { left: 0; top: 0; width: 235px; height: 100px; background: var(--purple-mid); }
  .mission__quote { left: 12px; top: 18px; width: 220px; color: var(--purple-light); font-size: 15px; font-weight: 700; line-height: 18.5px; }
  .mission .feature { left: 8px; border: 0; }
  .mission__title { left: 8px; top: 212px; font-size: 27px; font-weight: 700; color: var(--purple-soft); }
  .goal { position: absolute; left: 6px; display: flex; align-items: center; gap: 12px; }
  .goal__num { width: 44px; height: 44px; border-radius: 50%; background: var(--purple-mid); color: #cfc6ec; font-size: 26px; font-weight: 700; display: flex; align-items: center; justify-content: center; padding-top: 3px; }
  .goal__text { font-size: 16px; font-weight: 800; line-height: 19px; }
</style>
</head>
<body>

<!-- Outside of the tri-fold -->
<section class="spread spread--outside">
  <div class="panel works">
    <svg class="photo" width="230" height="190" role="img" aria-label="Photo of hexagon tiles showing devices over a blue server background">
      <defs><linearGradient id="techA" x1="0" y1="0" x2="1" y2="1"><stop offset="0" stop-color="#2a3d6a"/><stop offset=".5" stop-color="#5f86b8"/><stop offset="1" stop-color="#1e2a4a"/></linearGradient></defs>
      <path d="M0 0H230V118C180 128 120 150 60 168C30 176 10 172 0 168Z" fill="url(#techA)"/>
    </svg>
    <h2 class="abs works__title">How Quillon KELP Works</h2>
    <div class="abs works__copy">
      <p>Think of Quillon KELP as excellent GPS for your data. Slow data is a logistics problem, and Quillon KELP provides the smartest way to get data from one place to another, as quickly as possible, every time.</p>
      <p>How is it possible to increase productivity, keep precise control, and always move at optimal speed?</p>
      <p>RVT uses heuristics to abstract the complexity involved, which we pair with deep endpoint intelligence to achieve high-speed data transport and orchestration. And as you progress, Quillon KELP will learn and improve its process.</p>
      <p>Our simple UI creates an easy-to-use workflow that still allows granule control at the object level, allowing either a technical DBA or someone with no programming knowledge to move data on their terms, when they need it.</p>
    </div>
  </div>

  <div class="panel contact">
    <svg class="photo" width="232" height="140" role="img" aria-label="Photo of hands tapping tablets among hexagon tiles">
      <defs><linearGradient id="techB" x1="0" y1="0" x2="1" y2="1"><stop offset="0" stop-color="#3a5588"/><stop offset=".6" stop-color="#8aa7cf"/><stop offset="1" stop-color="#2a3d6a"/></linearGradient></defs>
      <path d="M0 0H232V10C225 60 190 110 120 120C70 126 30 124 0 122Z" fill="url(#techB)"/>
      <path d="M0 122C30 124 70 126 120 120C190 110 225 60 232 10" fill="none" stroke="var(--purple)" stroke-width="4"/>
    </svg>
    <div class="abs brandmark"><span class="brandmark__name">Quillon</span><span class="brandmark__product">KELP</span></div>
    <div class="abs contact__copy">
      <p>Quillon KELP is data transport optimization, designed to save time, save money, and efficiently accelerate your work with Big Data.</p>
      <p>Many customers struggle with how to achieve business objectives from constantly expanding Big Data. Legacy systems often don’t deliver the speed and scale necessary to achieve a good ROI.</p>
    </div>
    <div class="abs contact__rule"></div>
    <p class="abs contact__cta">CONTACT US TO LEARN HOW WE CAN HELP YOU</p>
    <p class="abs contact__demo">Build, Provision, Ship<br>See for Yourself, Schedule a Demo</p>
    <p class="abs contact__phone">
      <svg width="14" height="24" viewBox="0 0 14 24" aria-hidden="true"><rect x="1" y="1" width="12" height="22" rx="2" fill="none" stroke="#1b1b22" stroke-width="2"/><line x1="5" y1="19" x2="9" y2="19" stroke="#1b1b22" stroke-width="2"/></svg>
      (555) 214-6870
    </p>
    <div class="band">
      <svg class="abs" style="left:0;top:0" width="232" height="46" aria-hidden="true"><path d="M0 46C0 20 10 0 40 0H232V46Z" fill="var(--purple-soft)"/></svg>
      <p class="band__url">www.quillonkelp.com</p>
    </div>
  </div>

  <div class="panel cover">
    <div class="abs brandmark"><span class="brandmark__name">Quillon</span><span class="brandmark__product">KELP</span></div>
    <svg class="photo" style="top:98px" width="239" height="402" role="img" aria-label="Photo of a businessman in a suit with a glowing cloud network diagram">
      <defs><radialGradient id="suit" cx=".5" cy=".45" r=".6"><stop offset="0" stop-color="#8fa6c8"/><stop offset=".5" stop-color="#3a4763"/><stop offset="1" stop-color="#1c2233"/></radialGradient></defs>
      <path d="M0 40C40 10 110 -5 170 20C230 50 250 150 225 260C205 340 170 390 150 402H0Z" fill="url(#suit)"/>
    </svg>
    <div class="band cover__band">
      <p class="cover__tag">Effortless Movement of Data</p>
      <p class="cover__url">www.quillonkelp.com</p>
    </div>
  </div>
</section>

<!-- Inside of the tri-fold -->
<section class="spread spread--inside">
  <div class="panel intro">
    <svg class="photo" width="233" height="180" role="img" aria-label="Photo of two engineers working in a server room">
      <defs><linearGradient id="room" x1="0" y1="0" x2="1" y2="1"><stop offset="0" stop-color="#4a5f86"/><stop offset=".5" stop-color="#6e7f9c"/><stop offset="1" stop-color="#2a3550"/></linearGradient></defs>
      <path d="M0 0H233V130C200 180 160 160 120 150C70 138 30 140 0 150Z" fill="url(#room)"/>
    </svg>
    <h2 class="abs intro__title">Quillon KELP</h2>
    <p class="abs intro__sub">Effortless Movement of Data</p>
    <div class="abs intro__copy">
      <p>Quillon KELP is data transport optimization, designed to save time, save money, and efficiently accelerate your work with Big Data.</p>
      <p>Many customers struggle with how to achieve business objectives from constantly expanding Big Data. Legacy systems often don’t deliver the speed and scale necessary to achieve a good ROI.</p>
      <p>We believe the movement of data is key. Movement holds many untapped areas for improvement. Increase productivity, keep precise control, and always move at optimal speed.</p>
      <p>KELP is the fastest software on the market today to achieve effortless movement of data and data structures.</p>
    </div>
    <div class="band">
      <svg class="abs" style="left:0;top:0" width="233" height="32" aria-hidden="true"><path d="M0 0H200C220 0 230 20 233 32H0Z" fill="var(--purple-mid)"/></svg>
      <p class="band__url">www.quillonkelp.com</p>
    </div>
  </div>

  <div class="panel benefits">
    <svg class="photo" width="233" height="150" role="img" aria-label="Photo of server racks with a hand pointing at equipment">
      <defs><linearGradient id="rack" x1="0" y1="0" x2="1" y2="0"><stop offset="0" stop-color="#5e6f8e"/><stop offset=".6" stop-color="#2a3550"/><stop offset="1" stop-color="#141a2a"/></linearGradient></defs>
      <path d="M0 0H233V70C200 110 160 130 100 148C60 150 30 140 0 120Z" fill="url(#rack)"/>
    </svg>
    <h2 class="abs benefits__title">Achieve Transport</h2>
    <p class="abs benefits__sub">Optimization to Increase ROI</p>
    <div class="feature" style="top:196px">
      <h3 class="feature__head">Optimize the Cloud</h3>
      <ul class="checklist"><li>Gain productivity in complex environments</li><li>Move structure, as well as data</li><li>Understand endpoint to endpoint</li></ul>
    </div>
    <div class="feature" style="top:326px; padding-top:4px">
      <h3 class="feature__head">Optimize Migration</h3>
      <ul class="checklist"><li>Upgrade to the cloud in record time</li><li>Solve peak workload problems</li><li>Move at a fraction of the cost</li></ul>
    </div>
    <div class="feature" style="top:443px; padding-top:4px">
      <h3 class="feature__head">Optimize Knowledge</h3>
      <ul class="checklist"><li>Empower all data workers</li><li>Easily orchestrate movement</li><li>No programming necessary</li></ul>
    </div>
  </div>

  <div class="panel mission">
    <svg class="abs" style="left:0;top:0" width="235" height="110" aria-hidden="true"><path d="M0 0H235V102H30C15 102 5 110 0 110Z" fill="var(--purple-mid)"/></svg>
    <p class="abs mission__quote">Quillon is the craft of records. And Quillon KELP is the craft of record transit.</p>
    <div class="feature" style="top:113px">
      <h3 class="feature__head">Optimize Productivity</h3>
      <ul class="checklist"><li>Abstract away complexity</li><li>Keep precise control</li><li>Always move at optimal speed</li></ul>
    </div>
    <h2 class="abs mission__title">Our Mission</h2>
    <div class="goal" style="top:252px"><span class="goal__num">1</span><span class="goal__text">MAXIMIZE VALUE</span></div>
    <div class="goal" style="top:322px"><span class="goal__num">2</span><span class="goal__text">EXTEND YOUR<br>CURRENT SYSTEM</span></div>
    <div class="goal" style="top:396px"><span class="goal__num">3</span><span class="goal__text">GAIN ACTIONABLE<br>BEACONS—FASTER</span></div>
    <div class="goal" style="top:469px"><span class="goal__num">4</span><span class="goal__text">PROTECT &amp;<br>LEVERAGE LEGACY IT</span></div>
  </div>
</section>

</body>
</html>
```